Technology solutions catalog

Were looking for a catalogue to supplement our website and corporate branding.

Our website will give you a good understanding of our products and services as well as our theme.

Our base colour and logo is red, white and grey.

www.voltrane.com.au

The aim of the catalogue is to showcase our business IT services & solutions. This will be a mix of education about the new solutions available to small and medium business today and how these solutions can increase productivity.

We would also like tip sections

This isn't all about selling but also about educating SMB's of the new and exciting IT solutions available today and having them book a free consult with us to discuss further about how we can help the business.

Solutions and area's that the catalogue will need to cover include

Front Cover -
-About us section, with our business contact information (1st page)
- Introduction. (2nd page)
-Communication Solutions - this includes Email, IP phones and business IT networks (2 pages)
- Data & Storage solutions (2 pages)
- Hardware (1 pages)
- Business IT health check list (1 page)
- Services and support offering (2 pages)
- Software & Popular cloud solutions (2 pages)
- Website / E-commerce solutions (2 pages)
Back cover

Based on two pages per solution the whole catalogue will be around 14 pages.

We don't need any text content done. We would like Headings on pages including page numbers. Footer please.

We're looking for a template that we can have our designer finish off by adding in some further product and service image and text.

Thank you for your consideration

Target Market(s)

IT for small and medium businesses

Industry/Entity Type

Supplement

Requirements
Must have
• Size A4
• Design supplied in Adobe indesign so we can edit and add our text and content
• Clean design

```html
<!DOCTYPE html>
<html lang="en">
<head>
<meta charset="utf-8">
<title>Data &amp; Storage solutions – catalogue spread</title>
<link href="https://fonts.googleapis.com/css2?family=Open+Sans:ital,wght@0,300;0,400;0,600;1,400&display=swap" rel="stylesheet">
<style>
:root{
  --red:#c3222a;
  --ink:#3a3a3a;
  --body:#666;
  --grey-page:#f0f0f1;
  --white:#fff;
  --quote-bg:#58585a;
  --footer:#2a2a2c;
  --backdrop:#dcdcdc;
  --ring:#e2e2e4;
}
*{margin:0;padding:0;box-sizing:border-box}
html,body{width:1200px;height:960px;overflow:hidden;background:var(--backdrop);font-family:"Open Sans",Arial,sans-serif}
.spread{position:absolute;left:86px;top:118px;width:1283px;height:906px;transform:scale(.8);transform-origin:0 0;background:var(--white);box-shadow:0 30px 40px rgba(0,0,0,.18)}
.page{position:absolute;top:0;height:865px;width:641px;overflow:hidden}
.page--left{left:0;background:var(--white)}
.page--right{left:641px;width:642px}
.accent-tab{position:absolute;left:240px;top:0;width:161px;height:12px;background:var(--red)}
.kicker{position:absolute;top:66px;width:100%;text-align:center;font-size:15px;color:#777;letter-spacing:.2px}
.title{position:absolute;top:100px;width:100%;text-align:center;font-size:44px;font-weight:400;color:var(--red)}
.intro{position:absolute;top:186px;left:60px;width:521px;text-align:center;font-size:15.5px;line-height:18px;color:var(--ink)}
.quote{position:absolute;left:0;top:290px;width:319px;height:289px;background:var(--quote-bg);color:#eee;font-style:italic;font-size:15px;line-height:18.2px;text-align:center;padding:60px 38px 0 50px}
.quote-mark{position:absolute;font-size:60px;font-style:normal;font-weight:600;color:#3f3f41;line-height:1;font-family:Georgia,serif}
.quote-mark--open{left:30px;top:18px}
.quote-mark--close{right:24px;bottom:-10px}
.photo{position:absolute;left:319px;top:290px;width:322px;height:289px;background:linear-gradient(135deg,#e9eef3 0%,#c9d4de 45%,#8e9db0 100%)}
.idea-badge{position:absolute;left:298px;top:267px;width:40px;height:40px;border-radius:50%;background:var(--red);border:2px solid #fff;display:flex;align-items:center;justify-content:center}
.section-title{position:absolute;width:100%;text-align:center;font-size:20px;color:var(--red)}
.benefit{position:absolute;width:270px;text-align:center}
.benefit h3,.feature h3{font-weight:400;color:var(--ink);font-size:16px;line-height:18px;margin-bottom:4px}
.benefit p,.feature p{font-size:10.2px;line-height:13px;color:var(--body)}
.band{position:absolute;left:0;width:642px}
.band--grey{background:var(--grey-page)}
.band--white{background:var(--white)}
.feature{position:absolute;width:180px;text-align:center}
.feature .icon{width:56px;height:56px;margin:0 auto 14px;border-radius:50%;background:var(--white);border:3px solid var(--ring);display:flex;align-items:center;justify-content:center}
.band--white .feature .icon{background:var(--white)}
.footer{position:absolute;left:0;top:865px;width:1283px;height:41px;background:var(--footer)}
.folio{position:absolute;top:0;width:40px;height:41px;background:var(--red);color:#fff;font-size:13px;line-height:41px;text-align:center}
.folio--left{left:0}
.folio--right{right:0}
.footer-url{position:absolute;right:60px;top:0;line-height:41px;color:#fff;font-size:11px;font-weight:600}
</style>
</head>
<body>
<div class="spread">
  <section class="page page--left">
    <div class="accent-tab"></div>
    <p class="kicker">YOUR CLOUD | YOUR DATA | YOUR WAY</p>
    <h1 class="title">Data &amp; Storage solutions</h1>
    <p class="intro">Voltrane Data Cloud offers you a high capacity storage medium that’s in your control, with the ability to easily share and secure your important business data.</p>

    <blockquote class="quote">
      <span class="quote-mark quote-mark--open">“</span>
      Voltrane Data Cloud keeps your data at your place of business and under your control. Think of VDC as your own private cloud. Using our specialised Network attached storage (NAS) device at your business, data can be securely shared to staff and customers from our easy to use online interface.
      <span class="quote-mark quote-mark--close">”</span>
    </blockquote>
    <div class="photo" role="img" aria-label="Photo of a smiling businessman using a smartphone in a bright office"></div>
    <div class="idea-badge">
      <svg width="20" height="20" viewBox="0 0 20 20" fill="none" stroke="#fff" stroke-width="1.6"><circle cx="10" cy="8" r="5.5"/><path d="M7.5 14h5M8 17h4M10 8v5"/></svg>
    </div>

    <h2 class="section-title" style="top:603px">Benefits to your business</h2>
    <div class="benefit" style="left:44px;top:652px"><h3>Your Private cloud</h3><p>With Voltrane Data Cloud you keep control of your data, it’s your own business private cloud. All your data is stored and managed from the NAS device at your office.</p></div>
    <div class="benefit" style="left:326px;top:652px"><h3>Sharing is simple</h3><p>Sharing documents with staff couldn’t be easier, through your online portal you have access to all your files.</p></div>
    <div class="benefit" style="left:44px;top:746px"><h3>Grows with your business</h3><p>Unlike cloud based solutions our solution offers you no storage limit or costs per user, our solution can be customised to suit your needs and can grow with your business.</p></div>
    <div class="benefit" style="left:326px;top:741px"><h3>Mobile Access</h3><p>Access your files from any internet connected device. Our solution allows you to access files and data on desktops, tablets and phones operating systems.</p></div>
  </section>

  <section class="page page--right">
    <div class="band band--grey" style="top:0;height:287px">
      <h2 class="section-title" style="top:64px">Centralise all business data</h2>
      <div class="feature" style="left:42px;top:100px">
        <div class="icon"><svg width="18" height="14" viewBox="0 0 18 14" fill="none" stroke="var(--red)" stroke-width="1.6"><path d="M2 7 4 2h10l2 5v5H2z"/><path d="M2 7h14"/><circle cx="13" cy="9.5" r=".8" fill="var(--red)"/></svg></div>
        <h3>All the space you need</h3><p>Your in full control, the capacity is dependent on your needs and budget and can be extended as required.</p></div>
      <div class="feature" style="left:231px;top:100px">
        <div class="icon"><svg width="20" height="14" viewBox="0 0 20 14" fill="none" stroke="var(--red)" stroke-width="2"><path d="M3 9V3h11M11 0l3 3-3 3M17 5v6H6M9 14l-3-3 3-3"/></svg></div>
        <h3>Data Protection</h3><p>Using the latest in RAID technology you get full data loss prevention. RAID mirrors your data across multiple hard drives giving you piece of mind.</p></div>
      <div class="feature" style="left:419px;top:100px">
        <div class="icon"><svg width="14" height="16" viewBox="0 0 14 16"><path d="M4 7V5a3 3 0 0 1 6 0v2" fill="none" stroke="var(--red)" stroke-width="1.8"/><rect x="2" y="7" width="10" height="8" rx="1" fill="var(--red)"/></svg></div>
        <h3>Data Encryption</h3><p>Protect your data through the use of banking grade encryption</p></div>
    </div>

    <div class="band band--white" style="top:287px;height:292px">
      <h2 class="section-title" style="top:30px">Share your data to any internet connected device</h2>
      <div class="feature" style="left:42px;top:82px">
        <div class="icon"><svg width="22" height="16" viewBox="0 0 22 16" fill="var(--red)"><circle cx="11" cy="4" r="3"/><circle cx="5" cy="5" r="2.3"/><circle cx="17" cy="5" r="2.3"/><path d="M5 15c0-4 3-6 6-6s6 2 6 6zM0 14c0-3 2-5 5-5l1 .3C4.5 10.5 4 12 4 14zM22 14c0-3-2-5-5-5l-1 .3c1.5 1.2 2 2.7 2 4.7z"/></svg></div>
        <h3>Share folders<br>and files easily</h3><p>Through your secure online portal you can easily share your data to anyone.</p></div>
      <div class="feature" style="left:231px;top:82px">
        <div class="icon"><svg width="12" height="16" viewBox="0 0 12 16" fill="none" stroke="var(--red)" stroke-width="1.6"><rect x="1" y="1" width="10" height="14" rx="1.5"/><path d="M5 12.5h2"/></svg></div>
        <h3>PC, Tablet &amp;<br>Phone</h3><p>Access your files from virtually any computer or mobile device. You can access all your data at the office or on the road.</p></div>
      <div class="feature" style="left:419px;top:82px">
        <div class="icon"><svg width="14" height="16" viewBox="0 0 14 16" fill="none" stroke="var(--red)" stroke-width="1.5"><path d="M1 1h8l4 4v10H1z"/><path d="M9 1v4h4"/></svg></div>
        <h3>Conflict<br>Handling</h3><p>If a file is uploaded that already exists. Users have the option to replace or rename a file and compare.</p></div>
    </div>

    <div class="band band--grey" style="top:579px;height:286px">
      <h2 class="section-title" style="top:24px">Keeping your data safe and secure</h2>
      <div class="feature" style="left:42px;top:67px">
        <div class="icon"><svg width="20" height="14" viewBox="0 0 20 14" fill="none" stroke="var(--red)" stroke-width="2"><path d="M3 9V3h11M11 0l3 3-3 3M17 5v6H6M9 14l-3-3 3-3"/></svg></div>
        <h3>RAID Protection</h3><p>Using the latest in RAID technology your data is copied across multiple drives, Data loss would require the failure of two drives at the same time which is statistically impossible.</p></div>
      <div class="feature" style="left:231px;top:67px">
        <div class="icon"><svg width="14" height="16" viewBox="0 0 14 16" fill="none" stroke="var(--red)" stroke-width="1.5"><path d="M1 3h12M5 3V1h4v2M2.5 3l1 12h7l1-12M5.5 6v6M8.5 6v6"/></svg></div>
        <h3>Undelete files</h3><p>Users can undelete a file that was accidentally deleted through the web interface. Simply select the files in the trash bin and they are returned to where they were deleted from, with file versions.</p></div>
      <div class="feature" style="left:419px;top:67px">
        <div class="icon"><svg width="18" height="16" viewBox="0 0 18 16" fill="var(--red)"><path d="M7 0h4v6h3l-5 5-5-5h3z"/><path d="M0 11h5l2 2h4l2-2h5v5H0z"/></svg></div>
        <h3>External Backup</h3><p>Our solution integrates with a external backup drives or off site backup for complete piece of mind and natural disaster protection.</p></div>
    </div>
  </section>

  <footer class="footer">
    <span class="folio folio--left">04</span>
    <span class="footer-url">www.voltrane.com.au</span>
    <span class="folio folio--right">05</span>
  </footer>
</div>
</body>
</html>
```